Coffee House With Cycling Theme Wants Business Cards

We want to create a business card for a coffee house that has a cycling theme. We expect to use the current logo on one side of the business card and we have been considering adding the words 'COFFEE HOUSE' underneath (see example). For the other side of the business card we want an interesting design with tag-line, address and social media links (the normal business card stuff). See examples provided but we are not fixed on having it exactly as shown, we are very open to great creative ideas. Please note our logo has the initials ‘RV' in orange embedded in the design and this must be retained. However, you can play with the words COFFEE HOUSE as well as use the orange color on the backside of the business card, as you see fit. For an image on the backside of the business card it can be a photo, hand-drawn or whatever but it must visually combine coffee and cycling in some way. The interior of the Coffee House will be reclaimed wood, rustic and have an urban feel to it with cycling artifacts hanging from the walls/ceiling, etc. Finally, it would be beneficial if the business card design elements can be easily used on flyers and other promotional assets. Good luck, we are looking forward to seeing your creative ideas.

Target Market(s)

Coffee lovers and cycling fans

Contact Information for Business Card

See project description.

Colors

Designer to choose colors to be used in the design.

Requirements
Must have
• Must use the current logo provided and combine a coffee and bike theme.
Nice to have
• Orange is used in current logo and could be used as an accent color on the backside of the business card.

```html
<!DOCTYPE html>
<html lang="en">
<head>
<meta charset="utf-8">
<title>RV Coffee House – Business Card</title>
<link rel="stylesheet" href="https://fonts.googleapis.com/css2?family=EB+Garamond:wght@600&family=Montserrat:wght@500;800&display=swap">
<style>
  :root {
    --backdrop: #9a9a9a;
    --card-white: #ffffff;
    --brand-orange: #f26a26;
    --charcoal: #3b3b3b;
    --espresso-dark: #120c08;
    --espresso-mid: #4a2f1c;
    --roast-light: #8a5b34;
    --cream: #ffffff;
  }
  * { margin: 0; padding: 0; box-sizing: border-box; }
  html, body { width: 1200px; height: 1000px; overflow: hidden; }
  body {
    background: var(--backdrop);
    position: relative;
    font-family: "Montserrat", Arial, sans-serif;
  }
  .card {
    position: absolute;
    box-shadow: 0 3px 8px rgba(0,0,0,0.35);
    overflow: hidden;
  }

  /* Front */
  .card-front {
    left: 265px; top: 67px; width: 672px; height: 402px;
    background: var(--card-white);
  }
  .brand-mark {
    position: absolute; left: 0; right: 0; top: 150px;
    text-align: center;
    color: var(--brand-orange);
    font-family: "Montserrat", Arial, sans-serif;
    font-weight: 800;
  }
  .brand-initials { font-size: 112px; line-height: 1; letter-spacing: 4px; }
  .brand-words { font-size: 30px; line-height: 1; margin-top: 14px; letter-spacing: 1px; }
  .contact-band {
    position: absolute; left: 0; bottom: 0; width: 100%; height: 52px;
    display: flex; color: var(--cream); font-size: 17px; font-weight: 500;
    letter-spacing: 0.4px;
  }
  .band-web {
    width: 336px; background: var(--brand-orange);
    display: flex; align-items: center; padding-left: 41px; gap: 8px;
  }
  .band-address {
    flex: 1; background: var(--charcoal);
    display: flex; align-items: center; padding-left: 32px; gap: 9px;
  }

  /* Back */
  .card-back {
    left: 262px; top: 527px; width: 677px; height: 406px;
  }
  .back-photo {
    position: absolute; inset: 0;
    background:
      radial-gradient(ellipse at 78% 60%, #a9916f 0%, #8c7556 18%, transparent 40%),
      radial-gradient(ellipse at 60% 30%, var(--roast-light) 0%, var(--espresso-mid) 45%, transparent 75%),
      linear-gradient(90deg, var(--espresso-dark) 0%, #2a1a10 35%, var(--espresso-mid) 70%, #3a2516 100%);
  }
  .tagline {
    position: absolute; left: 48px; top: 52px;
    font-family: "EB Garamond", Georgia, serif; font-weight: 600;
    font-size: 38px; line-height: 54px; color: var(--cream);
    letter-spacing: 0.5px;
  }
  .social {
    position: absolute; left: 50px; top: 260px; color: var(--cream);
  }
  .social-handle {
    display: flex; align-items: center; gap: 8px;
    font-size: 21px; font-weight: 500;
  }
  .social-dot {
    width: 22px; height: 22px; border: 2px solid var(--cream); border-radius: 5px;
  }
  .social-email { font-size: 16.5px; font-weight: 500; margin-top: 6px; }
</style>
</head>
<body>
  <section class="card card-front">
    <div class="brand-mark">
      <div class="brand-initials">RV</div>
      <div class="brand-words">COFFEE HOUSE</div>
    </div>
    <div class="contact-band">
      <div class="band-web">
        <svg width="20" height="20" viewBox="0 0 20 20" aria-hidden="true">
          <g fill="none" stroke="#fff" stroke-width="1.5">
            <circle cx="10" cy="10" r="8.5"/>
            <ellipse cx="10" cy="10" rx="3.8" ry="8.5"/>
            <line x1="1.5" y1="10" x2="18.5" y2="10"/>
            <line x1="3" y1="5.5" x2="17" y2="5.5"/>
            <line x1="3" y1="14.5" x2="17" y2="14.5"/>
          </g>
        </svg>
        <span>www.rvcoffeehouse.com</span>
      </div>
      <div class="band-address">
        <svg width="18" height="24" viewBox="0 0 18 24" aria-hidden="true">
          <path d="M9 0C4 0 0 4 0 9c0 6.5 9 15 9 15s9-8.5 9-15c0-5-4-9-9-9z" fill="#fff"/>
          <circle cx="9" cy="9" r="3.4" fill="#3b3b3b"/>
        </svg>
        <span>4471 Harbor Ave., Del Mar</span>
      </div>
    </div>
  </section>

  <section class="card card-back">
    <div class="back-photo" role="img" aria-label="Photo of a burlap sack overflowing with roasted coffee beans on a wooden table against a warm brown wall"></div>
    <p class="tagline">Great Coffee in a<br>Cycling Flavored<br>Ambiance</p>
    <div class="social">
      <div class="social-handle"><span class="social-dot"></span><span>rvcoffeehouse</span></div>
      <div class="social-email">sam@rvcoffeehouse.com</div>
    </div>
  </section>
</body>
</html>
```